I need to refresh my meeting minutes pages (2 of them)

I have 2 pages that need to be modernized with a new look and feel. I have attached the 2 pages that need the refresh. I am okay with one page submissions as long as the winner is willing to add the second page before payment :-) Any questions please let me know. The logo on the page is not ours but a sample of what client may give us.

```html
<!DOCTYPE html>
<html lang="en">
<head>
<meta charset="utf-8">
<title>Agenda Item Details</title>
<link href="https://fonts.googleapis.com/css2?family=Instrument+Sans:wght@400;500;600;700&display=swap" rel="stylesheet">
<style>
:root{
  --bg:#f7f7f7;
  --surface:#ffffff;
  --tile:#f4f4f4;
  --line:#e4e4e4;
  --ink:#1d1d1f;
  --muted:#6f6f73;
  --faint:#a8a8ac;
  --accent:#0a84f5;
  --link:#0a7be0;
}
*{box-sizing:border-box;margin:0;padding:0}
html,body{width:1200px;height:675px;overflow:hidden}
body{background:var(--bg);font-family:"Instrument Sans",sans-serif;color:var(--ink);position:relative}

.topbar{position:absolute;left:0;top:0;width:1200px;height:60px;border-bottom:1px solid var(--line)}
.brand{position:absolute;left:18px;top:20px;font-size:16.5px;font-weight:600;letter-spacing:-.2px}
.powered{position:absolute;right:18px;top:16px;font-size:9.3px;color:var(--muted);line-height:14px}
.powered a{color:var(--muted);text-decoration:underline}

.rail{position:absolute;left:18px;top:81px;width:60px}
.rail-item{height:60px;display:flex;flex-direction:column;align-items:center;justify-content:center;gap:5px;font-size:8.4px;color:var(--muted);border-radius:4px;margin-bottom:6px}
.rail-item svg{width:17px;height:17px;stroke:currentColor;fill:none;stroke-width:1.4}
.rail-item.active{background:var(--accent);color:#fff;height:54px}

.agenda-panel{position:absolute;left:96px;top:79px;width:300px;height:578px;background:var(--surface);border-radius:6px;overflow:hidden}
.search{height:38px;border-bottom:1px solid var(--line);display:flex;align-items:center;gap:11px;padding-left:12px;font-size:11px;color:var(--faint)}
.search svg{width:13px;height:13px;stroke:var(--ink);fill:none;stroke-width:1.6}
.scrollbar{position:absolute;left:293px;top:41px;width:3px;height:180px;border-radius:2px;background:#d8d8d8}
.agenda-list{padding:0 12px}
.section{border-top:1px solid var(--line);padding-bottom:9px}
.section:first-child{border-top:none}
.section-title{height:36px;display:flex;align-items:center;font-size:9.4px;font-weight:700;letter-spacing:.1px}
.section:first-child .section-title{height:35px}
.item{min-height:32px;background:var(--tile);border-radius:3px;margin-bottom:1.3px;display:flex;align-items:center;padding:7px 10px 7px 36px;position:relative;font-size:11px;line-height:13.5px}
.item svg{position:absolute;left:12px;top:50%;margin-top:-6px;width:12px;height:12px;fill:none;stroke:currentColor;stroke-width:1.3}
.item.current{background:var(--accent);color:#fff;font-weight:600}

.toolbar-btn{position:absolute;top:79px;height:33px;border:1px solid var(--line);background:var(--surface);border-radius:4px;display:flex}
.toolbar-btn span{width:35px;display:flex;align-items:center;justify-content:center}
.toolbar-btn span+span{border-left:1px solid var(--line)}
.toolbar-btn svg{width:13px;height:13px;fill:none;stroke:var(--ink);stroke-width:1.5}
.pager{left:432px}
.print{left:521px}
.share{left:1146px}

.page-title{position:absolute;left:432px;top:136px;font-size:19px;font-weight:600;letter-spacing:-.2px}
.details{position:absolute;left:432px;top:182px;width:750px;height:269px;background:var(--surface);border-radius:6px;padding:0 18px}
.row{height:50.3px;border-bottom:1px solid var(--line);display:flex;align-items:center;font-size:11px}
.row dt{width:192px;font-weight:500}
.row dd{color:#333}
.attachment{margin-top:18px;height:32px;background:var(--tile);border-radius:3px;display:flex;align-items:center;padding:0 13px 0 12px;font-size:11px}
.attachment svg{width:12px;height:12px;fill:none;stroke:var(--muted);stroke-width:1.3;margin-right:12px}
.attachment a{color:var(--link);font-weight:500;text-decoration:none;flex:1}
.attachment .size{color:var(--muted)}
</style>
</head>
<body>
<header class="topbar">
  <div class="brand">ClientLogo</div>
  <div class="powered">Powered by:<br><a>MeetingDesk</a>® A Verity Brand, © 2002-2025</div>
</header>

<nav class="rail">
  <div class="rail-item"><svg viewBox="0 0 24 24"><circle cx="12" cy="12" r="10"/><path d="M12 6.5l1.7 3.6 3.8.4-2.9 2.6.8 3.8L12 15l-3.4 1.9.8-3.8-2.9-2.6 3.8-.4z"/></svg>Featured</div>
  <div class="rail-item"><svg viewBox="0 0 24 24"><circle cx="12" cy="5" r="2.5"/><circle cx="7" cy="11" r="2.2"/><circle cx="17" cy="11" r="2.2"/><rect x="3" y="14" width="18" height="7" rx="1"/><path d="M12 14v7"/></svg>Meetings</div>
  <div class="rail-item active"><svg viewBox="0 0 24 24"><rect x="3" y="5" width="17" height="15" rx="2"/><path d="M3 10h17M8 3v4M15 3v4"/><circle cx="17" cy="17" r="4" fill="#0a84f5"/><path d="M17 15v2l1.3 1"/></svg>Agenda</div>
  <div class="rail-item"><svg viewBox="0 0 24 24"><rect x="5" y="3" width="14" height="18" rx="2"/><circle cx="12" cy="12" r="3"/><path d="M9 3v3h6V3"/></svg>Policies</div>
</nav>

<aside class="agenda-panel">
  <div class="search"><svg viewBox="0 0 24 24"><circle cx="10" cy="10" r="7"/><path d="M15 15l6 6"/></svg>Search Agenda</div>
  <div class="scrollbar"></div>
  <div class="agenda-list">
    <section class="section">
      <div class="section-title">*R* WELCOME</div>
      <div class="item">Wireless Access For Guests</div>
    </section>
    <section class="section">
      <div class="section-title">*R* CALL TO ORDER</div>
      <div class="item">Pledge Of Allegiance</div>
      <div class="item">Roll Call</div>
    </section>
    <section class="section">
      <div class="section-title">RIDGEVIEW PROUD</div>
      <div class="item"><svg viewBox="0 0 24 24"><path d="M5 2h10l4 4v16H5z"/><path d="M8 10h8M8 14h8M8 18h8"/></svg>Northfield Hockey Coach</div>
      <div class="item"><svg viewBox="0 0 24 24"><path d="M5 2h10l4 4v16H5z"/><path d="M8 10h8M8 14h8M8 18h8"/></svg>Teaching Professions - Future Teachers State Competition</div>
    </section>
    <section class="section">
      <div class="section-title">*R* INFORMATION TO THE BOARD</div>
      <div class="item">Superintendent - ACES/PAGE/First Step</div>
      <div class="item"><svg viewBox="0 0 24 24"><path d="M5 2h10l4 4v16H5z"/><path d="M8 10h8M8 14h8M8 18h8"/></svg>ACES</div>
      <div class="item current"><svg viewBox="0 0 24 24"><path d="M5 2h10l4 4v16H5z"/><path d="M8 10h8M8 14h8M8 18h8"/></svg>PAGE</div>
      <div class="item"><svg viewBox="0 0 24 24"><path d="M5 2h10l4 4v16H5z"/><path d="M8 10h8M8 14h8M8 18h8"/></svg>First Step</div>
    </section>
    <section class="section">
      <div class="section-title">*R* COMMUNICATION(S)</div>
      <div class="item">Correspondence</div>
    </section>
  </div>
</aside>

<div class="toolbar-btn pager">
  <span><svg viewBox="0 0 24 24"><path d="M15 5l-7 7 7 7"/></svg></span>
  <span><svg viewBox="0 0 24 24"><path d="M9 5l7 7-7 7"/></svg></span>
</div>
<div class="toolbar-btn print"><span><svg viewBox="0 0 24 24"><path d="M7 9V3h10v6"/><rect x="3" y="9" width="18" height="8" rx="2"/><rect x="7" y="14" width="10" height="7"/></svg></span></div>
<div class="toolbar-btn share"><span><svg viewBox="0 0 24 24"><circle cx="18" cy="5" r="3"/><circle cx="6" cy="12" r="3"/><circle cx="18" cy="19" r="3"/><path d="M8.6 10.5l6.8-4M8.6 13.5l6.8 4"/></svg></span></div>

<h1 class="page-title">Agenda Item Details</h1>

<main class="details">
  <dl>
    <div class="row"><dt>Meeting</dt><dd>April 10, 2025 - Regular Meeting Agenda</dd></div>
    <div class="row"><dt>Category</dt><dd>*R* INFORMATION TO THE BOARD</dd></div>
    <div class="row"><dt>Subject</dt><dd>PAGE</dd></div>
    <div class="row"><dt>Type</dt><dd>-</dd></div>
  </dl>
  <div class="attachment">
    <svg viewBox="0 0 24 24"><path d="M5 2h10l4 4v16H5z"/><path d="M8 10h8M8 14h8M8 18h8"/></svg>
    <a>2025-04-10 - Ridgeview Proud - PAGE (1).pdf</a>
    <span class="size">40 KB</span>
  </div>
</main>
</body>
</html>
```